Business card for Full Stable Works Vanhoorne

I would like to have me designed an professional business card with my existing logo for my company called : full stable works vanhoorne gcv.
I prefer a two sided business card with on the back side only the horses head and the website : fswvanhoorne-example.eu
Only one colour shouldbe all right.
The logo must appear in a nic professional way on the business card.

Other suggestion are welcome.

All copy wrights must be released by the designer after we have selected a final design.

Target Market(s)

Equestrian businesses

Industry/Entity Type

Business

Contact Information for Business Card

Gerard Vanhoorne
Title: zaakvoerder
Full Stable Works Vanhoorne GCV
Lindekouter 47
B - 9999 Voorbeeldegem
België
Phone: + 32 400 98 76 10
Mail: gerard@fswvanhoorne-example.eu

Font styles to use
Serif

Requirements
Must have
• My own logo
• See attached files
• Website: fswvanhoorne-example.eu

```html
<!DOCTYPE html>
<html lang="nl">
<head>
<meta charset="utf-8">
<title>Full Stable Works Vanhoorne – Visitekaartje</title>
<link rel="stylesheet" href="https://fonts.googleapis.com/css2?family=Noto+Serif:wght@400;700&display=swap">
<style>
  :root {
    --page: #2b2b2b;
    --card-dark: #050505;
    --card-light: #ffffff;
    --ink: #1a1a1a;
    --ink-soft: #333333;
    --silver: #cfcfcf;
    --rule: #8a8a8a;
    --ghost: #ececec;
  }
  * { box-sizing: border-box; margin: 0; padding: 0; }
  html, body { width: 1200px; height: 900px; overflow: hidden; }
  body {
    background: var(--page);
    font-family: "Noto Serif", Georgia, serif;
    position: relative;
  }
  .card {
    position: absolute;
    left: 300px;
    width: 600px;
    height: 343px;
    border-radius: 22px;
    overflow: hidden;
  }
  .card--back { top: 70px; background: var(--card-dark); }
  .card--front { top: 487px; background: var(--card-light); }

  .back-name {
    position: absolute;
    left: 0; right: 0; top: 112px;
    text-align: center;
    color: var(--silver);
    font-size: 30px;
    font-weight: 700;
    letter-spacing: 1px;
    line-height: 1.2;
  }
  .back-web {
    position: absolute;
    left: 0; right: 0; bottom: 34px;
    text-align: center;
    color: #f2f2f2;
    font-size: 15px;
  }

  .ghost-mark {
    position: absolute;
    left: 250px; top: 40px;
    width: 250px; height: 250px;
    border-radius: 50%;
    background: var(--ghost);
  }
  .brand {
    position: absolute;
    left: 38px; top: 170px;
    width: 300px;
    color: var(--ink);
    font-size: 26px;
    font-weight: 700;
    line-height: 1.15;
    display: flex;
    align-items: center;
    gap: 12px;
  }
  .brand-dot {
    flex: none;
    width: 22px; height: 22px;
    border-radius: 50%;
    background: var(--ink);
  }
  .divider {
    position: absolute;
    left: 352px; top: 60px;
    width: 1px; height: 200px;
    background: var(--rule);
  }
  .contact {
    position: absolute;
    left: 372px; top: 58px;
    color: var(--ink-soft);
    font-size: 14px;
    line-height: 1.5;
  }
  .contact-name { font-size: 19px; color: var(--ink); }
  .contact-title { margin-bottom: 10px; }
  .contact-line { display: flex; align-items: center; gap: 8px; font-size: 13px; }
  .contact-line svg { width: 12px; height: 12px; flex: none; }
</style>
</head>
<body>
  <section class="card card--back" aria-label="Achterzijde">
    <div class="back-name">Full Stable Works<br>Vanhoorne</div>
    <div class="back-web">www.fswvanhoorne-example.eu</div>
  </section>

  <section class="card card--front" aria-label="Voorzijde">
    <div class="ghost-mark" aria-hidden="true"></div>
    <div class="brand"><span class="brand-dot"></span><span>Full Stable Works Vanhoorne</span></div>
    <div class="divider"></div>
    <div class="contact">
      <div class="contact-name">Gerard Vanhoorne</div>
      <div class="contact-title">Zaakvoerder</div>
      <div>Lindekouter 47</div>
      <div>B - 9999 Voorbeeldegem</div>
      <div>België</div>
      <div class="contact-line">
        <svg viewBox="0 0 12 12"><path d="M3 1l2 2-1 1.5c.7 1.4 1.8 2.5 3.5 3.5L9 7l2 2-1.5 2C5 10.5 1.5 7 1 2.5z" fill="#333"/></svg>
        <span>+ 32 400 98 76 10</span>
      </div>
      <div class="contact-line">
        <svg viewBox="0 0 12 12"><rect x="1" y="2.5" width="10" height="7" fill="none" stroke="#333"/><path d="M1 2.5l5 4 5-4" fill="none" stroke="#333"/></svg>
        <span>gerard@fswvanhoorne-example.eu</span>
      </div>
      <div class="contact-line">
        <svg viewBox="0 0 12 12"><circle cx="6" cy="6" r="5" fill="none" stroke="#333"/><ellipse cx="6" cy="6" rx="2.2" ry="5" fill="none" stroke="#333"/><path d="M1 6h10" stroke="#333"/></svg>
        <span>www.fswvanhoorne-example.eu</span>
      </div>
    </div>
  </section>
</body>
</html>
```